High School Rowing Club - duplicate example provided

Build web site based on example provided. We would like you to copy the general layout of the Corlinder rowing web site but insert our info (Maple Ridge Western).
Target Market(s)
High School Parents & Students
Industry/Entity Type
School
Number of Pages Required
5+ page
Font styles to use
Serif
Colors
Designer to choose colors to be used in the design.
Requirements
Must have
- Plug in for payment option (coinvale?) Parents will be making payments using this options.
- Online Registration Form - Please copy http://corlinderpaddlehub.com/ registration form inserting the basics. Please do not include their specific items at the bottom.
- Generally, Copy the format of http://corlinderpaddlehub.com/ to build our site.
Nice to have
- Include the photos we attached. Use "slider" format/style. Include our facebook page on the home/main page: Maple Ridge Western High School Rowing Team.
- Our content should work for 5 pages (tabs)
- Make sure to copy the green color from our current high school rowing website. http://www.mrwoars.org/

```html
<!DOCTYPE html>
<html lang="en">
<head>
<meta charset="utf-8">
<title>Coaches Info – Maple Ridge Western Rowing</title>
<link href="https://fonts.googleapis.com/css2?family=Oswald:wght@500;600&family=Roboto:wght@400;500&display=swap" rel="stylesheet">
<style>
:root{
  --header-top:#9aa39a;
  --header-bg:#4a564c;
  --green-dark:#1d5a2c;
  --green:#2f7a3e;
  --green-bright:#3e9a4d;
  --band:#a9cc98;
  --page:#dbe9d2;
  --rule:#8aa883;
  --text:#1c1f1c;
  --white:#ffffff;
  --footer:#22582f;
  --footer-bar:#1a4424;
  --photo-a:#5f7a5c;
  --photo-b:#2f4a33;
}
*{margin:0;padding:0;box-sizing:border-box}
html,body{width:1200px;height:3774px;overflow:hidden}
body{background:var(--page);font-family:"Roboto",sans-serif;color:var(--text);position:relative}

.site-header{position:absolute;left:0;top:0;width:1200px;height:140px;background:linear-gradient(var(--header-top) 0,var(--header-top) 30px,var(--header-bg) 30px)}
.nav{position:absolute;top:96px;font-family:"Oswald",sans-serif;font-weight:500;font-size:22px;color:var(--white);letter-spacing:.5px}
.nav span{position:absolute;white-space:nowrap}
.brand{position:absolute;left:0;width:1200px;top:92px;display:flex;align-items:center;justify-content:center;gap:10px;font-family:"Oswald",sans-serif;font-weight:500;font-size:24px;color:var(--white);text-transform:uppercase;letter-spacing:.5px}
.brand .dot{width:14px;height:14px;border-radius:50%;background:var(--white)}
.btn{position:absolute;top:24px;height:40px;font-family:"Oswald",sans-serif;font-weight:500;font-size:20px;color:var(--white);display:flex;align-items:center;justify-content:center}
.btn.reg{left:788px;width:175px;background:var(--green-bright)}
.btn.contact{left:1001px;width:131px;border:2px solid var(--white);background:var(--green)}

.title-band{position:absolute;left:0;top:160px;width:1200px;height:62px;background:var(--band);display:flex;align-items:center;justify-content:center;font-family:"Oswald",sans-serif;font-weight:600;font-size:38px;color:var(--green)}

.coach{position:absolute;left:0;width:1200px}
.photo{position:absolute;width:220px;height:335px;background:linear-gradient(160deg,var(--photo-a),var(--photo-b))}
.coach.left .photo{left:70px}
.coach.right .photo{left:913px}
.name{font-family:"Oswald",sans-serif;font-weight:600;font-size:38px;line-height:40px;color:var(--green-dark);text-transform:uppercase}
.role{font-family:"Oswald",sans-serif;font-weight:600;font-size:20px;line-height:24px;color:var(--green);text-transform:uppercase}
.bio{font-size:15.5px;line-height:21px;margin-top:10px}
.coach.left .body{position:absolute;left:342px;width:790px}
.coach.right .body{position:absolute;left:60px;width:835px;text-align:right}
.email{position:absolute;display:flex;align-items:center;gap:12px;font-family:"Oswald",sans-serif;font-weight:500;font-size:20px;color:var(--green-dark);text-transform:uppercase;white-space:nowrap}
.email svg{flex:none}
.rule{position:absolute;left:60px;width:1080px;height:2px;background:var(--rule)}

.site-footer{position:absolute;left:0;top:3397px;width:1200px;height:377px;background:var(--footer);color:var(--white)}
.foot-brand{position:absolute;left:30px;top:70px;width:260px;display:flex;align-items:center;justify-content:center;gap:10px;font-family:"Oswald",sans-serif;font-weight:500;font-size:26px;text-transform:uppercase}
.foot-brand .dot{width:16px;height:16px;border-radius:50%;background:var(--white)}
.foot-about{position:absolute;left:30px;top:148px;width:250px;font-family:"Oswald",sans-serif;font-weight:500;font-size:16px;line-height:21px;text-transform:uppercase}
.foot-col{position:absolute;top:34px}
.foot-col h3{font-family:"Oswald",sans-serif;font-weight:500;font-size:22px;text-transform:uppercase;padding-bottom:4px;border-bottom:2px solid var(--white);display:inline-block}
.socials{display:flex;gap:16px;margin-top:16px}
.socials span{width:36px;height:36px;background:var(--white);border-radius:4px}
.foot-text{font-family:"Oswald",sans-serif;font-weight:500;font-size:17px;line-height:22px;text-transform:uppercase;margin-top:16px;width:380px}
.links{list-style:none;margin-top:10px;font-family:"Oswald",sans-serif;font-weight:500;font-size:20px;line-height:32px;text-transform:uppercase}
.links li::before{content:"\25C6";font-size:13px;margin-right:14px;vertical-align:2px}
.copyright{position:absolute;left:0;bottom:0;width:1200px;height:34px;background:var(--footer-bar);display:flex;align-items:center;justify-content:center;font-size:18px;font-weight:500}
</style>
</head>
<body>

<header class="site-header">
  <div class="btn reg">REGISTRATION</div>
  <div class="btn contact">CONTACT</div>
  <nav class="nav">
    <span style="left:20px">HOME</span>
    <span style="left:163px">NEW OR INTERESTED ?</span>
    <span style="left:410px">COACHES</span>
    <span style="left:785px">PARENTS INFO</span>
    <span style="left:988px">SPONSORSHIPS</span>
  </nav>
  <div class="brand"><span class="dot"></span>MRW Crew</div>
</header>

<div class="title-band">COACHES INFO</div>

<section class="coach left" style="top:295px">
  <div class="photo" role="img" aria-label="Portrait photo of head coach Garrett Solano"></div>
  <div class="body" style="top:22px">
    <div class="name">Garrett Solano</div>
    <div class="role">Head Coach</div>
    <p class="bio">Garrett has been involved in rowing for 13 years. He began rowing at Maple Ridge Western in the spring of 2004 during his junior year. He spent the following two summers rowing in a competitive summer program in the Grand Rapids area. Garrett attended Lakeshore Valley University where he stroked the Varsity 8+ for 4 years, twice competed at the Royal Thamesbury Regatta in Thamesbury, England, and spent one summer in the senior development camp at Kestrel Rowing Club in Philadelphia. He graduated from LVU in 2009 with a BS in Biomedical Sciences. For the last three years he coached the Lakeshore Valley Freshmen men, with one bronze medalist Lightweight 8 and one 4th place Heavyweight 8 in the Heron Cup Regatta in Philadelphia. He comes back to the Maple Ridge program with the intention of providing guidance and structure to a historied program to bring it to the next level.</p>
  </div>
  <div class="email" style="right:68px;top:22px"><svg width="24" height="18" viewBox="0 0 24 18"><rect x="1" y="1" width="22" height="16" fill="none" stroke="#1d5a2c" stroke-width="2"/><path d="M1 1l11 9 11-9" fill="none" stroke="#1d5a2c" stroke-width="2"/></svg>gsolano@brightmail.com</div>
</section>
<div class="rule" style="top:667px"></div>

<section class="coach right" style="top:695px">
  <div class="photo" role="img" aria-label="Portrait photo of varsity women coach Nadia Solano"></div>
  <div class="body" style="top:0">
    <div class="name">Nadia Solano</div>
    <div class="role">Varsity Women</div>
    <p class="bio">Nadia began her rowing career at Upper Peninsula State University, after two years of being a scholarship volleyball player at Riverbend Community College. After her novice season she transferred to Lakeshore Valley University, where she double majored in Psychology and Criminal Justice. While rowing at LVU, she won two National Championships, and was invited to the Under 23 National Team Identification Camp, and placed 3rd at the prestigious Head of the Meridian Regatta. In her senior season, Nadia was honored as a 1st Team All-American athlete at the CRAA National Championships, in Gainesville, GA. Nadia will be coaching a bit from the sidelines this Spring, as she and Garrett welcomed their first child, a girl, to their family in March.</p>
  </div>
  <div class="email" style="right:305px;top:295px"><svg width="24" height="18" viewBox="0 0 24 18"><rect x="1" y="1" width="22" height="16" fill="none" stroke="#1d5a2c" stroke-width="2"/><path d="M1 1l11 9 11-9" fill="none" stroke="#1d5a2c" stroke-width="2"/></svg>nadia.solano@brightmail.com</div>
</section>
<div class="rule" style="top:1057px"></div>

<section class="coach left" style="top:1087px">
  <div class="photo" role="img" aria-label="Portrait photo of varsity men coach Colin Dorsett"></div>
  <div class="body" style="top:0">
    <div class="name">Colin Dorsett</div>
    <div class="role">Varsity Men Coach</div>
    <p class="bio">Colin rowed in high school and rowed every seat. He continued that flexibility by continuing to row in every seat while a rower at LVU. Coach Dorsett started coaching at MRW in 2015. This will be Coach Dorsett's second year as Varsity Men's coach.</p>
  </div>
  <div class="email" style="left:342px;top:214px"><svg width="24" height="18" viewBox="0 0 24 18"><rect x="1" y="1" width="22" height="16" fill="none" stroke="#1d5a2c" stroke-width="2"/><path d="M1 1l11 9 11-9" fill="none" stroke="#1d5a2c" stroke-width="2"/></svg>cdorsett@brightmail.com</div>
</section>
<div class="rule" style="top:1452px"></div>

<section class="coach right" style="top:1480px">
  <div class="photo" role="img" aria-label="Portrait photo of varsity men coach Harper Dorsett"></div>
  <div class="body" style="top:0">
    <div class="name">Harper Dorsett</div>
    <div class="role">Varsity Men Coach</div>
    <p class="bio">Harper attended Elmhurst Pioneer High School and rowed bow seat. She continued her rowing career in college, where she rowed as a coxswain for the Varsity Men's 8+. In 2010 Harper coached the fall "Learn to Row" program at Westbrook High School in Washington, DC. She joined the MRW coaching team in Spring 2016, and coaches alongside her husband, Colin Dorsett.</p>
  </div>
  <div class="email" style="right:305px;top:295px"><svg width="24" height="18" viewBox="0 0 24 18"><rect x="1" y="1" width="22" height="16" fill="none" stroke="#1d5a2c" stroke-width="2"/><path d="M1 1l11 9 11-9" fill="none" stroke="#1d5a2c" stroke-width="2"/></svg>harperdorsett@brightmail.com</div>
</section>
<div class="rule" style="top:1850px"></div>

<section class="coach left" style="top:1874px">
  <div class="photo" role="img" aria-label="Portrait photo of assistant varsity women coach Jenna Delacroix"></div>
  <div class="body" style="top:0">
    <div class="name">Jenna Delacroix</div>
    <div class="role">Asst. Coach Varsity Women</div>
    <p class="bio">Jenna attended Harbor Bay High School in Harbor Bay, MI. Jenna participated in various sports in high school, but her high school did not have a rowing team, so she was not able to compete in rowing. She was introduced to rowing at LVU, where she attended college. She became quickly intrigued by the sport, and became a coxswain. Jenna had a great experience at LVU and looks forward to sharing her enthusiasm and knowledge with the MRW rowers. This is Coach Jenna's first foray into coaching, as she helps out Coach Solano with the women's varsity squad.</p>
  </div>
  <div class="email" style="right:68px;top:0"><svg width="24" height="18" viewBox="0 0 24 18"><rect x="1" y="1" width="22" height="16" fill="none" stroke="#1d5a2c" stroke-width="2"/><path d="M1 1l11 9 11-9" fill="none" stroke="#1d5a2c" stroke-width="2"/></svg>delacroj@mail.lvu.edu</div>
</section>
<div class="rule" style="top:2234px"></div>

<section class="coach right" style="top:2264px">
  <div class="photo" role="img" aria-label="Portrait photo of assistant varsity women coach Hayley Engstrom"></div>
  <div class="body" style="top:0">
    <div class="name">Hayley Engstrom</div>
    <div class="role">Asst. Coach Varsity Women</div>
    <p class="bio">Hayley joined the MRW crew team as a freshman in the Fall of 2007, rowing in the 7th seat, and continued to row until she graduated in 2011. Hayley couldn't stay away from her favorite team and sport so she returned to the MRW rowing team in 2013 as an assistant coach for the novice women. The following year she took over as the novice women's head coach and is currently a coach with the Varsity women.</p>
  </div>
  <div class="email" style="right:305px;top:295px"><svg width="24" height="18" viewBox="0 0 24 18"><rect x="1" y="1" width="22" height="16" fill="none" stroke="#1d5a2c" stroke-width="2"/><path d="M1 1l11 9 11-9" fill="none" stroke="#1d5a2c" stroke-width="2"/></svg>engstroh@mail.lvu.edu</div>
</section>
<div class="rule" style="top:2629px"></div>

<section class="coach left" style="top:2654px">
  <div class="photo" role="img" aria-label="Portrait photo of sculling coach Tobias Fenwick"></div>
  <div class="body" style="top:0">
    <div class="name">Tobias Fenwick</div>
    <div class="role">Sculling Coach</div>
    <p class="bio">Tobias joined the MRW Rowing program, first as a volunteer in 2011 then Boosters Board Member through 2014, as his children began the sport. Tobias was a high school and collegiate swimmer at Kent River Junior College, swimming in the National Championships in 1989. Tobias and Head Coach Garrett Solano together began the winter training program. Tobias was an Assistant Coach with the Varsity Men in 2014 and in Spring of 2015, Tobias helped coach the Novice women. The 2016 season found Tobias helping get the MRW sculling program up and running. His willingness to head up the sculling, has allowed MRW crew to get more rowers in boats and make the team even more competitive.</p>
  </div>
  <div class="email" style="right:68px;top:0"><svg width="24" height="18" viewBox="0 0 24 18"><rect x="1" y="1" width="22" height="16" fill="none" stroke="#1d5a2c" stroke-width="2"/><path d="M1 1l11 9 11-9" fill="none" stroke="#1d5a2c" stroke-width="2"/></svg>tfenwick@brightmail.com</div>
</section>
<div class="rule" style="top:3019px"></div>

<section class="coach right" style="top:3049px">
  <div class="photo" role="img" aria-label="Portrait photo of assistant novice women coach Olive Dekker"></div>
  <div class="body" style="top:0">
    <div class="name">Olive Dekker</div>
    <div class="role">Asst. Coach Novice Women</div>
    <p class="bio">Olive joined the MRW crew team as a freshman in 2007, rowing 5 seat, and continued to row all four years of high school. She currently attends LVU and is graduating Spring 2017. She started coaching with MRW in 2012 as a novice coach and continues to help the novice women become highly successful in their boats.</p>
  </div>
  <div class="email" style="right:305px;top:295px"><svg width="24" height="18" viewBox="0 0 24 18"><rect x="1" y="1" width="22" height="16" fill="none" stroke="#1d5a2c" stroke-width="2"/><path d="M1 1l11 9 11-9" fill="none" stroke="#1d5a2c" stroke-width="2"/></svg>dekkero@mail.lvu.edu</div>
</section>

<footer class="site-footer">
  <div class="foot-brand"><span class="dot"></span>MRW Crew</div>
  <p class="foot-about">This site is designed by the team, for the purpose of providing any and all pertinent information with regards to the daily operations and activities of the organization.</p>

  <div class="foot-col" style="left:377px">
    <h3>Follow Us</h3>
    <div class="socials" aria-label="Social media links"><span></span><span></span><span></span><span></span></div>
    <p class="foot-text">The Maple Ridge Western rowing team practices out of the Maple Ridge boathouse located at 1250 Riverside Lane Alder</p>
    <h3 style="margin-top:14px;border:none;padding:0">Contact Us</h3>
    <div class="email" style="position:static;color:var(--white);font-size:17px;margin-top:6px"><svg width="24" height="18" viewBox="0 0 24 18"><rect x="1" y="1" width="22" height="16" fill="#ffffff"/><path d="M1 1l11 9 11-9" fill="none" stroke="#22582f" stroke-width="2"/></svg>admin@mrwoars.org</div>
  </div>

  <div class="foot-col" style="left:793px">
    <h3>Useful Links</h3>
    <ul class="links">
      <li>Home</li>
      <li>About Us</li>
      <li>FAQ's</li>
      <li>Coaches</li>
      <li>Parents Info</li>
      <li>Sponsorships</li>
    </ul>
  </div>

  <div class="copyright">&copy; Copyright-2017 MRWOARS.ORG</div>
</footer>

</body>
</html>
```